chocolate bar wrapper

Need a design for a new line of chocolate bars being sold at new retail candy store concept called PLINKTREATS. There will be many flavors including Dark Chocolate, Milk Chocolate, Dark Chocolate Espresso, Milk Chocolate Smores, Dark Chocolate Strawberry Champagne, Dark Chocolate Sea Salt, Dark Chocolate Chipotle, etc. Size of bar is 3 inches x 6 5/8 inches.

Please visit PLINKTREATS.EXAMPLE

Industry/Entity Type

Retail

```html
<!DOCTYPE html>
<html lang="en">
<head>
<meta charset="utf-8">
<title>Milk Chocolate Bar Wrapper</title>
<link rel="stylesheet" href="https://fonts.googleapis.com/css2?family=Righteous&display=swap">
<style>
  :root {
    --cocoa-deep: #3d2413;
    --cocoa-mid: #5e3a1c;
    --cocoa-glow: #a8743f;
    --ribbon-pink: #e0177f;
    --label-white: #ffffff;
    --label-shadow: #000000;
  }
  html, body {
    margin: 0;
    padding: 0;
    width: 1200px;
    height: 543px;
    overflow: hidden;
    background: var(--cocoa-deep);
  }
  .wrapper {
    display: block;
    width: 1200px;
    height: 543px;
  }
  .flavor-name {
    font-family: "Righteous", sans-serif;
    font-size: 150px;
    fill: var(--label-white);
  }
  .flavor-shadow {
    fill: var(--label-shadow);
  }
  .ribbon {
    fill: none;
    stroke: var(--ribbon-pink);
    stroke-width: 4;
  }
</style>
</head>
<body>
<svg class="wrapper" viewBox="0 0 1200 543" xmlns="http://www.w3.org/2000/svg">
  <defs>
    <linearGradient id="cocoa-band" x1="0" y1="0" x2="0" y2="1">
      <stop offset="0" style="stop-color: var(--cocoa-deep)"/>
      <stop offset="0.45" style="stop-color: var(--cocoa-mid)"/>
      <stop offset="0.85" style="stop-color: var(--cocoa-glow)"/>
      <stop offset="1" style="stop-color: var(--cocoa-mid)"/>
    </linearGradient>
  </defs>

  <rect class="backdrop" width="1200" height="543" style="fill: var(--cocoa-deep)"/>
  <path class="middle-band" fill="url(#cocoa-band)"
        d="M0,113 C150,40 400,45 600,70 S950,120 1200,75 L1200,490 C1050,470 900,360 700,385 S200,440 0,380 Z"/>

  <path class="ribbon ribbon-top" d="M0,113 C150,40 400,45 600,70 S950,120 1200,75"/>
  <path class="ribbon ribbon-bottom" d="M0,380 C200,440 500,420 700,385 S1050,470 1200,490"/>

  <g class="flavor-title">
    <text class="flavor-name flavor-shadow" x="408" y="222" textLength="392" lengthAdjust="spacingAndGlyphs">MILK</text>
    <text class="flavor-name" x="415" y="215" textLength="392" lengthAdjust="spacingAndGlyphs">MILK</text>
    <text class="flavor-name flavor-shadow" x="106" y="420" textLength="972" lengthAdjust="spacingAndGlyphs">CHOCOLATE</text>
    <text class="flavor-name" x="113" y="413" textLength="972" lengthAdjust="spacingAndGlyphs">CHOCOLATE</text>
  </g>
</svg>
</body>
</html>
```